Create a banner for me that embodies my health and well being package.

I am an intuitive counselor with a busy practice helping clients to shift their blocks and move forward in their lives.
I have created a package called '9 paths home again'
I am wanting a banner to put on my website page, facebook page and to use as a letter head in mailouts.
My ideal clients are those who want to create change in their lives and who invest money in themselves and their personal and spiritual growth.
I am different to regular life coaches as my sessions have a spiritual twist to them creating much deeper change in my clients.
I would like the banner to be mainly font with the title of the progam: 9 Paths Home Again (no other wording) (something along the lines of the Blackjack font) and that ties in with the theme of my website. I'm not sure what else I want with it and am looking for ideas.
Website:
www.quillorabalancecare.com.au
I also have a current facebook page for the business:
https://www.facebook.com/Quillora-Balance-Care-402715938846102/
(Note: I am about to drop my logo and business name and move to using my own name - the rest of the website will remain the same).
I have attached a doc with the draft of what wording will be on the website page any advertising will link to, to give you an idea of what the program is about.

Target Market(s)

People who invest money on themselves who are looking to improve their emotional well being and creating change in their life. Majority are middle aged women (also younger females and some men)

Industry/Entity Type

Health And Wellness

Font styles to use
Other font styles liked:
• I like Blackjack and Amienne. Along those lines.

Requirements
Must have
• Attractive, modern and GREAT font.
Nice to have
• Surprise me with something amazing!
• I love the colours in the 2 images I have up loaded as they represent the heart chakra colours. They could be a feature on the banner or blurred into the background.
Should not have
• Even though my work is quite spiritual I don't want it to look woo woo (meaning airy fairy spiritual stuff!)

```html
<!DOCTYPE html>
<html lang="en">
<head>
<meta charset="utf-8">
<title>9 Paths Home Again</title>
<link rel="stylesheet" href="https://fonts.googleapis.com/css2?family=Kaushan+Script&family=Dancing+Script:wght@500&display=swap">
<style>
  :root {
    --blush: #fde6dc;
    --frame: #f1cdbd;
    --sage: #6f8a3e;
    --rose: #d2387a;
    --bloom-pink: #ec8fb4;
    --bloom-leaf: #7fa05a;
  }
  html, body {
    margin: 0;
    padding: 0;
    overflow: hidden;
    background: var(--blush);
  }
  .banner {
    position: relative;
    width: 1200px;
    height: 548px;
    overflow: hidden;
    background: var(--blush);
  }
  .banner__frame {
    position: absolute;
    inset: 0;
  }
  .banner__florals {
    position: absolute;
  }
  .banner__florals--left {
    left: 0;
    top: 0;
    width: 340px;
    height: 390px;
  }
  .banner__florals--right {
    right: 0;
    top: 0;
    width: 330px;
    height: 180px;
  }
  .banner__title {
    position: absolute;
    left: 0;
    right: 0;
    top: 0;
    margin: 0;
    font-weight: normal;
    text-align: center;
  }
  .banner__title-number {
    position: absolute;
    left: 300px;
    width: 700px;
    top: 78px;
    text-align: center;
    font-family: "Kaushan Script", cursive;
    font-size: 176px;
    line-height: 1;
    color: var(--sage);
    letter-spacing: 2px;
  }
  .banner__title-tagline {
    position: absolute;
    left: 300px;
    width: 700px;
    top: 318px;
    text-align: center;
    font-family: "Dancing Script", cursive;
    font-weight: 500;
    font-size: 128px;
    line-height: 1;
    color: var(--rose);
  }
</style>
</head>
<body>
  <div class="banner">
    <svg class="banner__frame" width="1200" height="548" viewBox="0 0 1200 548" aria-hidden="true">
      <g fill="none" stroke="var(--frame)" stroke-width="4" stroke-linecap="round">
        <line x1="385" y1="24" x2="815" y2="24"/>
        <line x1="1170" y1="170" x2="1170" y2="440"/>
        <line x1="28" y1="420" x2="28" y2="548"/>
        <line x1="1170" y1="480" x2="1170" y2="548"/>
      </g>
    </svg>

    <svg class="banner__florals banner__florals--left" viewBox="0 0 340 390" role="img" aria-label="Cascade of pink roses and green leaves spilling from the top-left corner">
      <defs>
        <linearGradient id="bloomLeft" x1="0" y1="0" x2="1" y2="1">
          <stop offset="0" stop-color="var(--bloom-pink)" stop-opacity="0.55"/>
          <stop offset="0.55" stop-color="var(--bloom-leaf)" stop-opacity="0.35"/>
          <stop offset="1" stop-color="var(--bloom-pink)" stop-opacity="0.3"/>
        </linearGradient>
      </defs>
      <path d="M0 0 H120 C110 90 150 190 240 270 C290 300 330 300 335 320 C300 360 200 360 150 340 C90 330 40 360 0 390 Z" fill="url(#bloomLeft)"/>
    </svg>

    <svg class="banner__florals banner__florals--right" viewBox="0 0 330 180" role="img" aria-label="Spray of pink roses and leaves in the top-right corner">
      <defs>
        <linearGradient id="bloomRight" x1="1" y1="0" x2="0" y2="1">
          <stop offset="0" stop-color="var(--bloom-pink)" stop-opacity="0.55"/>
          <stop offset="1" stop-color="var(--bloom-leaf)" stop-opacity="0.3"/>
        </linearGradient>
      </defs>
      <path d="M330 0 H20 C40 40 90 70 160 75 C220 80 250 120 300 170 L330 180 Z" fill="url(#bloomRight)"/>
    </svg>

    <h1 class="banner__title">
      <span class="banner__title-number">9 paths</span>
      <span class="banner__title-tagline">home again</span>
    </h1>
  </div>
</body>
</html>
```